Golf Brochure + Business Card Design Project – Larchmere Wellness.

Task Description

We are looking for a premium tri-fold brochure (8.5x11 letter, folded) plus a new business card design for Larchmere Wellness. Both need to look polished, elegant, and professional — something that would feel at home in a golf club environment.

Brochure Scope:
• Tri-fold brochure promoting our new golf-specific services
• Incorporate brand colors: deep hunter green, cream, and gold accents
• Clean, modern typography (professional, not playful)
• Layout will follow the copy provided (final copy attached, no rewriting needed)
• Imagery: mature golfers (50+), golf lifestyle shots, no generic stocky images
• Include QR code placement linking to booking page
• Deliverables: print-ready PDF with bleed/crop (CMYK), high-res PDF (digital), and source file (InDesign or Illustrator)

Business Card Scope:
• Front + back design
• Consistent with brand colors and fonts
• Space for name, title, phone, email, and website
• Deliverables: print-ready PDF with bleed/crop (CMYK) + source file (AI or InDesign)
• If possible, provide editable template for future staff cards

Timeline:
• First draft within 5–7 days
• 2 rounds of revisions included

Budget:
$300 USD (total for both brochure + business card)

I’ll provide finalized copy if you accept the project.
Project description (paste this whole block in that box)

We need a premium tri-fold brochure (8.5”×11” letter, folded) and a new business card design for Larchmere Wellness. This will be presented to golf course managers and members, so the look must be elegant, restrained, and country-club-classy.

Scope — Brochure
• Format: Tri-fold, 8.5”×11”. Please set 0.125” bleed on all sides and keep critical text ≥0.125–0.25” inside the trim.
• Purpose: Promote Larchmere Wellness’ golf-specific services for adults 50+.
• Copy: We will provide finalized copy in a Word doc after acceptance. No rewriting needed — please focus on layout and polish.
• Imagery (required):
• Golf-first images (ball on tee/green, mature golfers mid-swing, and golf course landscapes at golden hour).
• 1–2 real Larchmere Wellness gym photos on inside panels (trainer with client doing golf-relevant movement: stretch, rotation, balance).
• Visual style: Premium, quiet, lots of white/negative space, balanced grids; no clutter.
• Brand colors (required): Hunter Green #0C2E1F, Gold #CBA135, Cream #F5F2EB. Convert for CMYK print while preserving the look.
• Typography: Clean, legible serif + sans pairing (e.g., modern serif for headlines, humanist/neo-grotesk sans for body). You may propose suitable professional fonts; avoid playful/novelty fonts.
• Elements to include:
• Our logo (we will upload).
• QR code placement to booking page (we will supply the URL / QR asset).
• Simple icon treatment for the three complimentary options (Strength & Mobility, Stretch Therapy, Corelyn + Assessment).
• Deliverables:
• Print-ready PDF (CMYK, with bleed & crop marks, PDF/X-1a or PDF/X-4)
• High-res digital PDF (no bleed)
• Source file (InDesign or Illustrator) + packaged fonts/links or outlined type as appropriate.

Scope — Business Card
• Size: 3.5”×2” (US standard) with 0.125” bleed; keep text ≥0.125” from trim.
• Front/back design; consistent with brochure branding.
• Fields: Name, Title, Phone, Email, Website, Address; optional small QR on back.
• Deliverables: Print-ready PDF (CMYK, bleed & crops) + Source file (AI/INDD). Provide an editable template for staff names.

Process & Timing
• Initial concept for brochure + card within 5–7 days of acceptance.
• 2 rounds of revisions included.
• Please start with a clean layout concept using placeholder images/text blocks; we’ll drop in final copy/assets immediately after acceptance.

Stock & Licensing
• You may propose stock images that fit the brief (we’re fine approving Pictavault or equivalent). Please note any license fees separately if needed.

Usage Rights
• We require full usage rights to the final designs for print & digital.

Target Market(s)

Golfers 50+ in Victoria, BC: quality-oriented, health-conscious, want to play longer, stronger, and pain-free. Country-club aesthetic; expect polished, professional materials.

Industry/Entity Type

Health & Fitness — Golf Performance / Longevity Studio

Font styles to use
Serif
Sans Serif

Requirements
Must have
• • Golf-first imagery + 1–2 real Larchmere Wellness photos inside. • Brand colors: #0C2E1F (Hunter Green), #CBA135 (Gold), #F5F2EB (Cream). • Premium, restrained layout; ample negative space; no clutter. • Clean professional serif + sans type pairing; highly legible. • Space for logo and QR code (booking). • Correct print specs (bleed, crops, CMYK). • Deliverables: print-ready PDFs (brochure + card), digital PDF, source files.
Nice to have
• • Subtle texture or grain in backgrounds (very light) to add sophistication. • A second brochure cover variation (ball on tee vs. course landscape) at concept stage.
Should not have
• • Cheesy/posed “stocky” groups; overly young models; beer/alcohol imagery. • Over-saturated greens/blues; gimmicky gradients or clip art. • Generic fitness/bodybuilding shots unrelated to golf performance.

```html
<!DOCTYPE html>
<html lang="en">
<head>
<meta charset="utf-8">
<title>Larchmere Wellness – Business Card</title>
<link rel="stylesheet" href="https://fonts.googleapis.com/css2?family=Arimo:wght@400;700&family=Tinos&display=swap">
<style>
  :root {
    --hunter: #0c2e1f;
    --hunter-deep: #0a2619;
    --gold: #cba135;
    --gold-dark: #8a6a1c;
    --cream: #f5f2eb;
    --cream-shade: #e6e2da;
    --stage: #b3b3b3;
    --white: #ffffff;
  }
  * { margin: 0; padding: 0; box-sizing: border-box; }
  html, body { width: 953px; height: 1200px; overflow: hidden; }
  body {
    background: var(--stage);
    font-family: "Arimo", Arial, sans-serif;
    position: relative;
  }
  .card {
    position: absolute;
    left: 117px;
    width: 719px;
    height: 431px;
    overflow: hidden;
  }
  .card-front {
    top: 109px;
    background: radial-gradient(ellipse at 50% 45%, #12382a 0%, var(--hunter) 55%, var(--hunter-deep) 100%);
  }
  .card-back {
    top: 659px;
    background: linear-gradient(110deg, var(--cream-shade) 0%, var(--cream) 40%, var(--cream) 65%, var(--cream-shade) 100%);
  }

  /* front */
  .front-mark {
    position: absolute;
    left: 0; right: 0; top: 60px;
    display: flex; flex-direction: column; align-items: center;
  }
  .front-mark .ring {
    width: 118px; height: 118px;
    border: 4px solid var(--gold);
    border-radius: 50%;
  }
  .front-mark .brand {
    margin-top: 22px;
    color: var(--gold);
    font-weight: 700;
    font-size: 26px;
    letter-spacing: 5px;
    text-transform: uppercase;
  }
  .pillars {
    position: absolute;
    left: 0; right: 0; top: 292px; height: 47px;
    background: var(--gold);
  }
  .pillar {
    position: absolute; top: 0; line-height: 47px;
    transform: translateX(-50%);
    color: var(--hunter);
    font-weight: 700; font-size: 21px; letter-spacing: 1.5px;
  }
  .pillar-divider {
    position: absolute; top: 11px; width: 1px; height: 25px;
    background: var(--gold-dark);
  }
  .front-web {
    position: absolute; left: 0; right: 0; top: 374px;
    text-align: center;
    color: var(--white);
    font-size: 20px; letter-spacing: 4.5px;
  }
  .front-web .domain { color: var(--gold); font-weight: 700; }

  /* back */
  .back-shapes { position: absolute; inset: 0; }
  .back-brand {
    position: absolute; left: 48px; top: 158px; width: 150px;
    text-align: center;
    color: var(--hunter);
    font-weight: 700; font-size: 15px; letter-spacing: 2px; line-height: 1.35;
    text-transform: uppercase;
  }
  .person-name {
    position: absolute; left: 316px; top: 136px;
    font-family: "Tinos", "Times New Roman", serif;
    color: var(--gold);
    font-size: 36px; line-height: 1;
    white-space: nowrap;
  }
  .person-title {
    position: absolute; left: 318px; top: 181px;
    color: var(--white);
    font-size: 14px; letter-spacing: 1px;
  }
  .contact-list { position: absolute; left: 318px; top: 209px; list-style: none; }
  .contact-item {
    display: flex; align-items: center;
    height: 30px;
    color: var(--white);
    font-size: 17.5px;
  }
  .contact-item svg { width: 24px; height: 24px; margin-right: 10px; flex: none; }
</style>
</head>
<body>

<section class="card card-front" aria-label="Business card front">
  <div class="front-mark">
    <div class="ring"></div>
    <div class="brand">Larchmere Wellness</div>
  </div>
  <div class="pillars">
    <span class="pillar" style="left:144px">STRENGTH</span>
    <span class="pillar-divider" style="left:248px"></span>
    <span class="pillar" style="left:344px">MOBILITY</span>
    <span class="pillar-divider" style="left:441px"></span>
    <span class="pillar" style="left:549px">LONGEVITY</span>
  </div>
  <p class="front-web">www.<span class="domain">larchmerewellness</span>.biz</p>
</section>

<section class="card card-back" aria-label="Business card back">
  <svg class="back-shapes" width="719" height="431" viewBox="0 0 719 431">
    <rect class="band" x="0" y="110" width="719" height="220" fill="var(--hunter)"/>
    <polygon class="chevron-fold" points="250,80 279,110 236,110" fill="var(--gold-dark)"/>
    <polygon class="chevron" points="95,80 250,80 190,183 250,288 95,288 36,183" fill="var(--gold)"/>
    <polygon class="tab-fold" points="469,330 502,330 491,351" fill="var(--gold-dark)"/>
    <polygon class="tab" points="509,316 659,316 640,351 491,351" fill="var(--gold)"/>
  </svg>

  <div class="back-brand">Larchmere<br>Wellness</div>

  <h1 class="person-name">Clara-Jane Whitmore</h1>
  <p class="person-title">OWNER | LARCHMERE WELLNESS</p>

  <ul class="contact-list">
    <li class="contact-item">
      <svg viewBox="0 0 24 24" aria-hidden="true">
        <circle cx="12" cy="12" r="12" fill="var(--gold)"/>
        <path d="M8.6 6.5l1.8 2.4-1.1 1.3c.7 1.6 1.9 2.8 3.5 3.5l1.3-1.1 2.4 1.8-.9 2.1c-4.3-.2-8.1-4-8.3-8.3z" fill="var(--white)"/>
      </svg>
      250-555-0147
    </li>
    <li class="contact-item">
      <svg viewBox="0 0 24 24" aria-hidden="true">
        <circle cx="12" cy="12" r="12" fill="var(--gold)"/>
        <rect x="6" y="8" width="12" height="8.5" fill="var(--white)"/>
        <path d="M6 8l6 5 6-5" fill="none" stroke="var(--gold)" stroke-width="1.2"/>
      </svg>
      clara-jane@larchmerewellness.biz
    </li>
    <li class="contact-item">
      <svg viewBox="0 0 24 24" aria-hidden="true">
        <circle cx="12" cy="12" r="12" fill="var(--gold)"/>
        <g fill="none" stroke="var(--white)" stroke-width="1.3">
          <circle cx="12" cy="12" r="6"/>
          <ellipse cx="12" cy="12" rx="2.6" ry="6"/>
          <path d="M6 12h12M7 9h10M7 15h10"/>
        </g>
      </svg>
      www.larchmerewellness.biz
    </li>
  </ul>
</section>

</body>
</html>
```